Social Media Post – Promotion Announcement for Rick Hollis

Objective:
Create a professional and eye-catching social media post announcing the promotion of Rick Hollis to Vice President of Sales – Foodservice. The design should be modern, clean, and aligned with Danbury Sales & Marketing’s branding style (friendly, West Coast, professional). It should match our website:

www.danburysales.example

Key Requirements:

Include Rick Hollis’s photo (we will provide a high-resolution image).
Prominently display his name: “Rick Hollis.”
Prominently display his new title: “Vice President of Sales – Foodservice.”

A header or highlight that says something like: “Promotion Announcement” or “Congratulations!”

Design must be editable in Canva so we can reuse the template for future promotions.

Square format (1080x1080px) for Instagram/LinkedIn, but adaptable to landscape (1200x628px) if possible.

Style Guide / Preferences:

Colors: Incorporate Danbury Sales & Marketing brand blue (#0B64C0) along with white, gray, and/or complementary tones.

Fonts: Clean, modern sans-serif. Readable even on mobile.

Layout: Balanced between photo and text.

Option 1: Circular frame for the photo at center/top, text below.

Option 2: Split design with photo on one side and text on the other.

Tone: Professional, celebratory, approachable.

Deliverables:

Canva template file (editable).

Exported PNG/JPEG preview for review.

```html
<!DOCTYPE html>
<html lang="en">
<head>
<meta charset="utf-8">
<title>Promotion Announcement – Rick Hollis</title>
<link rel="stylesheet" href="https://fonts.googleapis.com/css2?family=Bebas+Neue&family=Dancing+Script:wght@600&family=Montserrat:wght@500;700&display=swap">
<style>
  :root {
    --brand-blue: #2f4fa3;
    --brand-blue-light: #6079bf;
    --brand-blue-mid: #4863ad;
    --gold: #fdbd1a;
    --gold-soft: #ffe39a;
    --cream: #fff6dc;
    --white: #ffffff;
    --photo-tone-a: #eceef2;
    --photo-tone-b: #b9a898;
  }
  * { box-sizing: border-box; margin: 0; padding: 0; }
  html, body { width: 1200px; height: 1200px; overflow: hidden; background: var(--white); }
  .post {
    position: relative;
    width: 1200px;
    height: 1200px;
    overflow: hidden;
    background: var(--white);
  }
  .post__backdrop { position: absolute; inset: 0; width: 1200px; height: 1200px; }
  .brand-name {
    position: absolute;
    top: 52px;
    left: 0;
    width: 100%;
    text-align: center;
    font-family: "Montserrat", sans-serif;
    font-weight: 700;
    font-size: 38px;
    letter-spacing: 1px;
    color: var(--brand-blue);
  }
  .headline {
    position: absolute;
    top: 118px;
    left: 0;
    width: 100%;
    text-align: center;
    font-family: "Dancing Script", cursive;
    font-weight: 600;
    font-size: 160px;
    line-height: 1.1;
    color: var(--brand-blue);
  }
  .portrait-ring {
    position: absolute;
    left: 302px;
    top: 302px;
    width: 598px;
    height: 598px;
    border-radius: 50%;
    background: linear-gradient(135deg, var(--gold) 0%, var(--gold) 55%, var(--gold-soft) 80%, var(--gold) 100%);
    padding: 27px;
  }
  .portrait-photo {
    width: 100%;
    height: 100%;
    border-radius: 50%;
    background: radial-gradient(circle at 50% 45%, var(--photo-tone-a) 0%, var(--photo-tone-a) 45%, var(--photo-tone-b) 100%);
  }
  .person-name {
    position: absolute;
    top: 948px;
    left: 0;
    width: 100%;
    text-align: center;
    font-family: "Bebas Neue", sans-serif;
    font-size: 200px;
    line-height: 1;
    letter-spacing: 4px;
    color: var(--white);
  }
  .person-title {
    position: absolute;
    top: 1122px;
    left: 0;
    width: 100%;
    text-align: center;
    font-family: "Montserrat", sans-serif;
    font-weight: 500;
    font-size: 41px;
    color: var(--gold);
  }
</style>
</head>
<body>
  <main class="post">
    <svg class="post__backdrop" viewBox="0 0 1200 1200" aria-hidden="true">
      <defs>
        <linearGradient id="cream-fade" x1="0" y1="0" x2="0" y2="1">
          <stop offset="0.45" stop-color="#ffffff"/>
          <stop offset="1" stop-color="#fff6dc"/>
        </linearGradient>
        <linearGradient id="deep-band" x1="0" y1="0" x2="1" y2="1">
          <stop offset="0" stop-color="#2f4fa3"/>
          <stop offset="0.6" stop-color="#3656aa"/>
          <stop offset="1" stop-color="#6a82c4"/>
        </linearGradient>
      </defs>
      <rect class="band-light" width="1200" height="1200" fill="#6079bf"/>
      <path class="band-deep" d="M0,820 C220,930 420,985 640,975 C900,960 1100,800 1200,560 V1200 H0 Z" fill="url(#deep-band)"/>
      <path class="band-mid" d="M0,770 C230,890 430,945 640,935 C900,920 1110,720 1200,420 V560 C1100,800 900,960 640,975 C420,985 220,930 0,820 Z" fill="#4863ad" opacity="0.55"/>
      <path class="field-cream" d="M0,0 H1200 V300 C1140,620 940,900 620,925 C380,945 170,860 0,745 Z" fill="url(#cream-fade)"/>
    </svg>

    <p class="brand-name">Danbury Sales &amp; Marketing</p>
    <h1 class="headline">Congratulations!</h1>

    <div class="portrait-ring">
      <div class="portrait-photo" role="img" aria-label="Portrait photo of Rick Hollis"></div>
    </div>

    <h2 class="person-name">Rick Hollis</h2>
    <p class="person-title">Vice President of Sales – Foodservice</p>
  </main>
</body>
</html>
```